Business Card for staff member of football club SC Brenval

I would like to get a business card template for all staff member of our soccer club.

The card should use as much as possible the 2 colors of the club : Red which is the main color and blue which is the alternative color. It can be balanced between the two like our logo.

I prefer simple and lean design.

Contact Information for Business Card

Bussiness card should have all main stuff as describe here below in must have.

Font styles to use
Sans Serif

Requirements
Must have
• Name : Laurent DESPRATIN
Fonction : Président
Mobile : +41 xx xxx xx xx
Email : first.lastname@scbrenval.ch
Adresse of the club : SC Brenval, 1873 Brenval
Website of the club : www.scbrenval.ch
Nice to have
• Version with and without picture of the staff member

A version for men, a version for women staff member.

```html
<!DOCTYPE html>
<html lang="en">
<head>
<meta charset="utf-8">
<title>SC Brenval – Staff Business Cards</title>
<link href="https://fonts.googleapis.com/css2?family=Signika:wght@300;400;600&display=swap" rel="stylesheet">
<style>
  :root {
    --red: #eb2039;
    --blue: #238acb;
    --white: #ffffff;
    --ink: #111315;
    --stage-edge: #2c3e66;
    --stage-centre: #0f5c86;
    --portrait: #0a0c0d;
  }
  * { box-sizing: border-box; margin: 0; padding: 0; }
  html, body { width: 1200px; height: 505px; overflow: hidden; }
  body {
    position: relative;
    background: radial-gradient(ellipse at 50% 50%, var(--stage-centre) 0%, #1f5279 45%, var(--stage-edge) 100%);
    font-family: "Signika", "Trebuchet MS", sans-serif;
  }
  .card {
    position: absolute;
    width: 334px;
    height: 191px;
    background: var(--white);
    overflow: hidden;
    --accent: var(--blue);
  }
  .card--red { --accent: var(--red); }
  .row-top { top: 44px; }
  .row-bottom { top: 270px; }
  .col-front { left: 45px; }
  .col-back { left: 438px; }
  .col-portrait { left: 821px; }

  .card__shape { position: absolute; inset: 0; width: 100%; height: 100%; }
  .card__shape path { fill: var(--accent); }

  .holder {
    position: absolute;
    left: 0; width: 250px; top: 6px;
    text-align: center;
    color: var(--white);
  }
  .holder__name { font-weight: 300; font-size: 18.5px; letter-spacing: 0.1px; line-height: 22px; }
  .holder__role {
    display: flex; align-items: center; justify-content: center;
    gap: 3px; margin-top: 0; padding: 0 35px 0 34px;
    font-weight: 300; font-size: 14px; line-height: 18px;
  }
  .holder__role::before, .holder__role::after {
    content: ""; flex: 1; height: 1.3px; background: var(--white);
  }

  .contact {
    position: absolute; left: 9px; top: 86px;
    list-style: none; color: var(--white);
    font-weight: 300; font-size: 11px; line-height: 15.6px;
  }
  .contact li:last-child { margin-top: 1.5px; }

  .club-mark {
    position: absolute;
    display: flex; flex-direction: column; align-items: center;
    color: var(--ink); font-weight: 600; text-align: center;
  }
  .club-mark__dot { border-radius: 50%; background: var(--accent); }
  .club-mark--small { left: 266px; top: 124px; width: 44px; font-size: 10px; line-height: 11px; gap: 4px; }
  .club-mark--small .club-mark__dot { width: 26px; height: 26px; }
  .club-mark--large { left: 120px; top: 30px; width: 122px; font-size: 22px; line-height: 24px; gap: 10px; }
  .club-mark--large .club-mark__dot { width: 78px; height: 78px; }

  .portrait {
    position: absolute; left: 168px; top: 38px; width: 128px; height: 153px;
    border-radius: 60px 60px 8px 8px;
    background: linear-gradient(180deg, #1a1d1f 0%, var(--portrait) 100%);
  }
</style>
</head>
<body>

  <!-- Blue set -->
  <section class="card row-top col-front">
    <svg class="card__shape" viewBox="0 0 718 410" preserveAspectRatio="none" aria-hidden="true">
      <path d="M0 0 H538 C556 70 562 200 522 282 C492 342 452 382 410 410 H0 Z"/>
      <path d="M556 0 H596 C614 90 592 210 534 298 C572 200 580 90 556 0 Z"/>
    </svg>
    <div class="holder">
      <p class="holder__name">Laurent DESPRATIN</p>
      <p class="holder__role">President</p>
    </div>
    <ul class="contact">
      <li>Mobile: +41 xx xxx xx xx</li>
      <li>E-mail: first.lastname@scbrenval.ch</li>
      <li>Website: www.scbrenval.ch</li>
      <li>Adresse of the club: SC Brenval, 1873 Brenval</li>
    </ul>
    <div class="club-mark club-mark--small"><span class="club-mark__dot"></span>SC Brenval</div>
  </section>

  <section class="card row-top col-back">
    <svg class="card__shape" viewBox="0 0 718 410" preserveAspectRatio="none" aria-hidden="true">
      <path d="M0 0 H122 C108 160 170 320 309 410 H0 Z"/>
      <path d="M146 0 H180 C164 100 168 200 185 295 C148 230 132 110 146 0 Z"/>
    </svg>
    <div class="club-mark club-mark--large"><span class="club-mark__dot"></span>SC Brenval</div>
  </section>

  <section class="card row-top col-portrait">
    <svg class="card__shape" viewBox="0 0 718 410" preserveAspectRatio="none" aria-hidden="true">
      <path d="M0 0 H122 C108 160 170 320 309 410 H0 Z"/>
      <path d="M146 0 H180 C164 100 168 200 185 295 C148 230 132 110 146 0 Z"/>
    </svg>
    <div class="portrait" role="img" aria-label="Portrait of a male staff member"></div>
  </section>

  <!-- Red set -->
  <section class="card card--red row-bottom col-front">
    <svg class="card__shape" viewBox="0 0 718 410" preserveAspectRatio="none" aria-hidden="true">
      <path d="M0 0 H538 C556 70 562 200 522 282 C492 342 452 382 410 410 H0 Z"/>
      <path d="M556 0 H596 C614 90 592 210 534 298 C572 200 580 90 556 0 Z"/>
    </svg>
    <div class="holder">
      <p class="holder__name">Laurent DESPRATIN</p>
      <p class="holder__role">President</p>
    </div>
    <ul class="contact">
      <li>Mobile: +41 xx xxx xx xx</li>
      <li>E-mail: first.lastname@scbrenval.ch</li>
      <li>Website: www.scbrenval.ch</li>
      <li>Adresse of the club: SC Brenval, 1873 Brenval</li>
    </ul>
    <div class="club-mark club-mark--small"><span class="club-mark__dot"></span>SC Brenval</div>
  </section>

  <section class="card card--red row-bottom col-back">
    <svg class="card__shape" viewBox="0 0 718 410" preserveAspectRatio="none" aria-hidden="true">
      <path d="M0 0 H122 C108 160 170 320 309 410 H0 Z"/>
      <path d="M146 0 H180 C164 100 168 200 185 295 C148 230 132 110 146 0 Z"/>
    </svg>
    <div class="club-mark club-mark--large"><span class="club-mark__dot"></span>SC Brenval</div>
  </section>

  <section class="card card--red row-bottom col-portrait">
    <svg class="card__shape" viewBox="0 0 718 410" preserveAspectRatio="none" aria-hidden="true">
      <path d="M0 0 H122 C108 160 170 320 309 410 H0 Z"/>
      <path d="M146 0 H180 C164 100 168 200 185 295 C148 230 132 110 146 0 Z"/>
    </svg>
    <div class="portrait" role="img" aria-label="Portrait of a female staff member"></div>
  </section>

</body>
</html>
```